professional looking data specialist website

I've recently had a new logo designed and I'm now looking to get a professional looking website built. This is for a new company that specialises in data. We look to support companies with business intelligence, report modelling, data governance to new european legislation (GDPR). We are offer consultancy or we can attend site and complete work when required. Our target arket is united kingdom wide and we are specifically aiming at small to medium sized companies.

Target Market(s)

small to medium enterprise companies from all industries

Industry/Entity Type

Professional Service

Coding

Coded - Design and coding required

Number of Pages Required

4 page

Font styles to use
Sans Serif

Colors

Designer to choose colors to be used in the design.

Requirements
Must have
• Professional look including the company logo, need to have ability to request more information from us so needs a inquiries page, seperate pages for the different offerings, data governance, report modelling, business intelligence implementation, data protection
Nice to have
• any website interaction, animation, etc
Should not have
• too many colours, too busy pages, must look professional

```html
<!DOCTYPE html>
<html lang="en">
<head>
<meta charset="utf-8">
<title>Meridata Ltd — Data Specialists</title>
<link href="https://fonts.googleapis.com/css2?family=Montserrat:wght@400;600;700&family=Open+Sans:wght@400;600&display=swap" rel="stylesheet">
<style>
:root{
  --blue:#1b6fc2;
  --blue-dark:#135aa3;
  --ink:#2b2f36;
  --text:#6f7680;
  --muted:#9aa1aa;
  --line:#e3e6ea;
  --grey:#f3f4f6;
  --white:#ffffff;
  --footer:#262a30;
  --footer-deep:#1c1f24;
}
*{box-sizing:border-box;margin:0;padding:0}
html,body{width:1200px;height:3956px;overflow:hidden}
body{font-family:"Open Sans",Arial,sans-serif;color:var(--text);background:var(--white);font-size:13px;line-height:1.6}
h1,h2,h3,h4,.nav a,.btn{font-family:"Montserrat",Arial,sans-serif}
.wrap{width:1040px;margin:0 auto;position:relative}
.eyebrow{color:var(--blue);font-family:"Montserrat",Arial,sans-serif;font-weight:600;font-size:13px;text-align:center}
.title{color:var(--ink);font-size:30px;font-weight:700;text-align:center;margin-top:4px}
.title::after{content:"";display:block;width:50px;height:3px;background:var(--blue);margin:12px auto 0}
.lead{text-align:center;max-width:720px;margin:18px auto 0;font-size:13px}
.btn{display:inline-block;background:var(--blue);color:var(--white);font-size:12px;font-weight:600;padding:10px 28px;border-radius:3px;letter-spacing:.5px}

/* header */
.site-header{height:112px;position:relative}
.brand{position:absolute;left:80px;top:26px;display:flex;align-items:center;gap:10px}
.brand-mark{width:30px;height:30px;background:var(--blue)}
.brand-name{font-family:"Montserrat",Arial,sans-serif;font-weight:700;font-size:24px;color:var(--blue)}
.contact-strip{position:absolute;right:80px;top:14px;display:flex;gap:26px;align-items:center;font-size:12px}
.contact-strip span{display:flex;align-items:center;gap:6px}
.pill{background:#8d949c;color:var(--white);padding:4px 16px;border-radius:14px;font-size:11px}
.nav{position:absolute;left:360px;right:80px;top:60px;height:34px;background:var(--blue);display:flex;align-items:center;padding:0 16px;gap:22px}
.nav a{color:var(--white);font-size:11px;font-weight:600;text-decoration:none}
.nav .search{margin-left:auto}

/* hero */
.hero{height:448px;position:relative;background:linear-gradient(100deg,#e9edf1 0%,#cfd6de 45%,#8f99a5 100%)}
.hero-copy{position:absolute;left:176px;top:80px;width:360px}
.hero h1{font-size:44px;line-height:1.15;color:var(--ink);font-weight:700}
.hero h1 em{color:var(--blue);font-style:normal}
.hero p{margin:18px 0 22px;font-size:13px;color:#4c535c}
.arrow{position:absolute;top:200px;width:26px;height:40px;background:rgba(0,0,0,.45);display:flex;align-items:center;justify-content:center}
.arrow.left{left:40px}.arrow.right{right:40px}

/* about */
.about{height:400px;padding-top:52px}
.about .eyebrow,.about .title{text-align:left}
.about .title::after{margin-left:0}
.about .lead{text-align:left;margin-left:0;max-width:1040px}
.features{display:grid;grid-template-columns:250px 250px;gap:26px 20px;margin-top:36px}
.feature{display:flex;gap:12px}
.feature svg{flex:none}
.feature h4{font-size:15px;color:var(--ink);font-weight:600}
.feature p{font-size:12px}
.about-photo{position:absolute;right:0;top:156px;width:440px;height:190px;background:linear-gradient(180deg,#f2f3f5,#c9ced5)}

/* services */
.services{height:420px;background:var(--blue);padding-top:50px;color:#d9e7f6}
.services .title{color:var(--white)}
.services .title::after{background:var(--white)}
.services .lead{color:#d9e7f6}
.service-grid{display:grid;grid-template-columns:repeat(4,1fr);gap:40px;margin-top:40px}
.service{text-align:center}
.service h3{font-size:16px;color:var(--white);margin:14px 0 8px;font-weight:600}
.service p{font-size:12px}
.service .more{display:inline-block;margin-top:10px;font-size:11px;color:var(--white);border-bottom:1px solid #fff}

/* assessment */
.assessment{height:540px;background:linear-gradient(180deg,#f1f2f4,#e6e9ec);padding-top:46px}
.cards{display:grid;grid-template-columns:repeat(4,1fr);gap:22px;margin-top:44px}
.card{background:var(--white);padding:30px 22px;text-align:center;box-shadow:0 2px 8px rgba(0,0,0,.06)}
.card h4{color:var(--ink);font-size:15px;margin:14px 0 8px;font-weight:600}
.card p{font-size:12px}

/* call back */
.callback{height:380px;padding-top:40px}
.form{margin-top:34px}
.row{display:grid;grid-template-columns:repeat(3,1fr);gap:30px}
.field{border-bottom:1px solid var(--line);padding:8px 0;font-size:12px;color:var(--muted)}
.field.message{margin-top:14px;height:60px}
.form .submit{display:block;width:max-content;margin:26px auto 0;border-radius:20px;padding:8px 40px}

/* advisors */
.advisors{height:580px;background:linear-gradient(180deg,#e8eaed,#cfd3d8);padding-top:40px}
.team{display:grid;grid-template-columns:repeat(3,1fr);gap:60px;margin:36px 60px 0}
.member{text-align:center}
.member-photo{height:240px;background:linear-gradient(180deg,#dfe2e6,#b9bfc6)}
.member h4{color:var(--ink);font-size:15px;margin-top:14px;font-weight:600}
.member .role{font-size:12px}
.dots{display:flex;justify-content:center;gap:10px;margin-top:8px}
.dots i{width:10px;height:10px;border-radius:50%;background:#7c848e}

/* cta */
.cta{height:110px;background:var(--blue-dark)}
.cta .wrap{display:flex;align-items:center;justify-content:space-between;height:110px;padding:0 60px}
.cta h3{color:var(--white);font-size:22px;font-weight:600}
.cta .btn{background:transparent;border:2px solid var(--white);border-radius:20px}

/* posts */
.posts{height:630px;padding-top:46px}
.post-grid{display:grid;grid-template-columns:420px 1fr;gap:30px;margin-top:36px}
.post-main .thumb{height:220px;background:linear-gradient(135deg,#dbe7f3,#8fb3d8)}
.post-main h3{color:var(--blue);font-size:19px;margin:14px 0 6px;font-weight:600}
.meta{font-size:11px;color:var(--muted);display:flex;gap:16px}
.post-main p{font-size:12px;margin-top:8px}
.post-list{display:flex;flex-direction:column;gap:16px}
.post-item{display:flex;gap:14px}
.post-item .thumb{width:110px;height:74px;flex:none;background:linear-gradient(135deg,#e4e8ec,#aab3bd)}
.post-item h4{color:var(--ink);font-size:14px;font-weight:600}
.post-item p{font-size:11px}

/* footer */
.site-footer{height:300px;background:var(--footer);padding-top:40px;color:#a9aeb5}
.footer-grid{display:grid;grid-template-columns:repeat(3,1fr);gap:40px}
.site-footer h4{color:var(--white);font-size:16px;font-weight:600;margin-bottom:18px}
.site-footer li{list-style:none;display:flex;gap:10px;align-items:center;font-size:12px;margin-bottom:10px}
.subscribe{display:flex;margin-top:16px}
.subscribe .input{flex:1;background:#383d44;height:34px;padding:8px;font-size:12px}
.subscribe .go{background:var(--blue);color:var(--white);width:50px;display:flex;align-items:center;justify-content:center;font-weight:600;font-size:12px}
.socials{display:flex;gap:8px}
.socials i{width:26px;height:26px;background:var(--blue)}
.footer-brand{display:flex;align-items:center;gap:8px;margin-top:24px}
.footer-brand .brand-mark{width:22px;height:22px}
.footer-brand span{font-family:"Montserrat",Arial,sans-serif;font-weight:700;font-size:20px;color:var(--blue)}
.bottom-bar{height:36px;background:var(--footer-deep);font-size:11px;color:#7f858d;display:flex;align-items:center;padding-left:80px}
</style>
</head>
<body>

<header class="site-header">
  <div class="brand"><span class="brand-mark"></span><span class="brand-name">Meridata Ltd</span></div>
  <div class="contact-strip">
    <span><svg width="12" height="12" viewBox="0 0 24 24"><path fill="#1b6fc2" d="M6.6 10.8a15 15 0 006.6 6.6l2.2-2.2a1 1 0 011-.25 11 11 0 003.6.6 1 1 0 011 1V20a1 1 0 01-1 1A17 17 0 013 4a1 1 0 011-1h3.5a1 1 0 011 1 11 11 0 00.6 3.6 1 1 0 01-.25 1z"/></svg>+44 000 000 0000</span>
    <span><svg width="12" height="12" viewBox="0 0 24 24"><rect x="2" y="5" width="20" height="14" rx="2" fill="#1b6fc2"/><path d="M3 6l9 7 9-7" stroke="#fff" stroke-width="2" fill="none"/></svg>info@meridata.co.uk</span>
    <span class="pill">+44 000 000 0000</span>
  </div>
  <nav class="nav">
    <a>HOME</a><a>ABOUT US</a><a>SERVICES</a><a>PRICING</a><a>RESOURCES</a><a>BLOG</a><a>CONTACT US</a>
    <svg class="search" width="14" height="14" viewBox="0 0 24 24"><circle cx="10" cy="10" r="7" stroke="#fff" stroke-width="2.5" fill="none"/><path d="M15 15l6 6" stroke="#fff" stroke-width="2.5"/></svg>
  </nav>
</header>

<section class="hero">
  <div role="img" aria-label="Photo of two smiling business professionals at a laptop" style="position:absolute;inset:0"></div>
  <div class="hero-copy">
    <h1>Grow Your Business With <em>Us</em></h1>
    <p>Clear data, sound reporting and practical guidance to help your small or medium business grow with confidence.</p>
    <span class="btn">LEARN MORE</span>
  </div>
  <span class="arrow left"><svg width="10" height="14" viewBox="0 0 10 14"><path d="M8 1L2 7l6 6" stroke="#fff" stroke-width="2" fill="none"/></svg></span>
  <span class="arrow right"><svg width="10" height="14" viewBox="0 0 10 14"><path d="M2 1l6 6-6 6" stroke="#fff" stroke-width="2" fill="none"/></svg></span>
</section>

<section class="about">
  <div class="wrap">
    <p class="eyebrow">About Us</p>
    <h2 class="title">Welcome to Meridata</h2>
    <p class="lead">We are a UK data consultancy supporting small and medium companies with business intelligence, report modelling and data governance. We work remotely as consultants or attend your site to complete the work whenever it is required.</p>
    <div class="features">
      <div class="feature"><svg width="34" height="34" viewBox="0 0 34 34"><circle cx="17" cy="17" r="16" fill="none" stroke="#1b6fc2" stroke-width="1.5"/><circle cx="17" cy="13" r="4" fill="#1b6fc2"/><path d="M10 25a7 7 0 0114 0z" fill="#1b6fc2"/></svg><div><h4>Who we are</h4><p>Data specialists with years of hands-on industry work.</p></div></div>
      <div class="feature"><svg width="34" height="34" viewBox="0 0 34 34"><circle cx="17" cy="17" r="16" fill="none" stroke="#1b6fc2" stroke-width="1.5"/><circle cx="17" cy="17" r="7" fill="none" stroke="#1b6fc2" stroke-width="2"/><circle cx="17" cy="17" r="2" fill="#1b6fc2"/></svg><div><h4>Our Mission</h4><p>Turning your data into decisions you can trust.</p></div></div>
      <div class="feature"><svg width="34" height="34" viewBox="0 0 34 34"><circle cx="17" cy="17" r="16" fill="none" stroke="#1b6fc2" stroke-width="1.5"/><path d="M8 17s4-6 9-6 9 6 9 6-4 6-9 6-9-6-9-6z" fill="none" stroke="#1b6fc2" stroke-width="2"/><circle cx="17" cy="17" r="2.5" fill="#1b6fc2"/></svg><div><h4>Our Vision</h4><p>Every growing business working with clear data.</p></div></div>
      <div class="feature"><svg width="34" height="34" viewBox="0 0 34 34"><circle cx="17" cy="17" r="16" fill="none" stroke="#1b6fc2" stroke-width="1.5"/><path d="M11 17l4 4 8-8" fill="none" stroke="#1b6fc2" stroke-width="2.5"/></svg><div><h4>Our Credits</h4><p>Trusted by firms across the United Kingdom.</p></div></div>
    </div>
    <div class="about-photo" role="img" aria-label="Photo of a business team standing together in suits"></div>
  </div>
</section>

<section class="services">
  <div class="wrap">
    <h2 class="title">Our Services</h2>
    <p class="lead">From strategy to delivery, we support every stage of your data journey.</p>
    <div class="service-grid">
      <div class="service"><svg width="54" height="54" viewBox="0 0 54 54"><circle cx="27" cy="27" r="25" fill="none" stroke="#fff" stroke-width="2"/><path d="M27 15l10 4v8c0 7-5 11-10 13-5-2-10-6-10-13v-8z" fill="none" stroke="#fff" stroke-width="2"/></svg><h3>Data Governance</h3><p>Policies and controls that keep your data accurate, secure and ready for new regulation.</p><span class="more">Read More</span></div>
      <div class="service"><svg width="54" height="54" viewBox="0 0 54 54"><circle cx="27" cy="27" r="25" fill="none" stroke="#fff" stroke-width="2"/><rect x="17" y="15" width="20" height="24" fill="none" stroke="#fff" stroke-width="2"/><path d="M21 22h12M21 27h12M21 32h8" stroke="#fff" stroke-width="2"/></svg><h3>Report Modelling</h3><p>Well-built reports and models that give your teams the figures they need, on time.</p><span class="more">Read More</span></div>
      <div class="service"><svg width="54" height="54" viewBox="0 0 54 54"><circle cx="27" cy="27" r="25" fill="none" stroke="#fff" stroke-width="2"/><path d="M17 37V29M24 37V22M31 37V26M38 37V17" stroke="#fff" stroke-width="3"/></svg><h3>Business Intelligence</h3><p>Dashboards and insight tools implemented to fit the way your business works.</p><span class="more">Read More</span></div>
      <div class="service"><svg width="54" height="54" viewBox="0 0 54 54"><circle cx="27" cy="27" r="25" fill="none" stroke="#fff" stroke-width="2"/><rect x="18" y="25" width="18" height="14" fill="none" stroke="#fff" stroke-width="2"/><path d="M21 25v-4a6 6 0 0112 0v4" fill="none" stroke="#fff" stroke-width="2"/></svg><h3>Data Protection</h3><p>Practical GDPR guidance so you handle personal data safely and lawfully.</p><span class="more">Read More</span></div>
    </div>
  </div>
</section>

<section class="assessment">
  <div class="wrap">
    <p class="eyebrow">Why Choose Us</p>
    <h2 class="title">Our Assessment</h2>
    <p class="lead">We begin every project with a clear review of your data, your reporting and your obligations, then agree a plan that suits your size and budget.</p>
    <div class="cards" style="grid-template-columns:repeat(3,1fr);margin:44px 40px 0">
      <div class="card"><svg width="44" height="44" viewBox="0 0 44 44"><path d="M22 36S8 27 8 17a7 7 0 0114-2 7 7 0 0114 2c0 10-14 19-14 19z" fill="none" stroke="#1b6fc2" stroke-width="2"/></svg><h4>We Deal With Love</h4><p>We care about every client and treat your data as carefully as our own.</p></div>
      <div class="card"><svg width="44" height="44" viewBox="0 0 44 44"><rect x="8" y="14" width="28" height="20" rx="2" fill="none" stroke="#1b6fc2" stroke-width="2"/><path d="M17 14v-4h10v4" fill="none" stroke="#1b6fc2" stroke-width="2"/></svg><h4>We Are Professional</h4><p>Qualified consultants working to clear standards and agreed timescales.</p></div>
      <div class="card"><svg width="44" height="44" viewBox="0 0 44 44"><path d="M22 7l4.5 9 10 1.5-7.2 7 1.7 10L22 30l-9 4.5 1.7-10-7.2-7 10-1.5z" fill="none" stroke="#1b6fc2" stroke-width="2"/></svg><h4>We Deliver Our Best</h4><p>Reliable results with support that continues after the work is done.</p></div>
    </div>
  </div>
</section>

<section class="callback">
  <div class="wrap">
    <p class="eyebrow">Free Consultation</p>
    <h2 class="title">Get A Call Back</h2>
    <p class="lead">Leave your details and one of our data specialists will call you back to talk through your needs, with no cost and no obligation.</p>
    <div class="form" style="margin:34px 40px 0">
      <div class="row"><div class="field">Name</div><div class="field">Email</div><div class="field">Phone</div></div>
      <div class="field message">Message</div>
      <span class="btn submit">SUBMIT</span>
    </div>
  </div>
</section>

<section class="advisors">
  <div class="wrap">
    <p class="eyebrow">Meet The Team</p>
    <h2 class="title">Our Advisors</h2>
    <p class="lead">Experienced advisors who combine technical skill with a clear understanding of how growing businesses run.</p>
    <div class="team">
      <div class="member"><div class="member-photo" role="img" aria-label="Portrait of advisor Clara Benson"></div><h4>Clara Benson</h4><p class="role">Data Consultant</p><div class="dots"><i></i><i></i><i></i><i></i></div></div>
      <div class="member"><div class="member-photo" role="img" aria-label="Portrait of advisor Tom Hadley"></div><h4>Tom Hadley</h4><p class="role">BI Specialist</p><div class="dots"><i></i><i></i><i></i><i></i></div></div>
      <div class="member"><div class="member-photo" role="img" aria-label="Portrait of advisor Nina Shaw"></div><h4>Nina Shaw</h4><p class="role">GDPR Advisor</p><div class="dots"><i></i><i></i><i></i><i></i></div></div>
    </div>
  </div>
</section>

<section class="cta">
  <div class="wrap">
    <h3>Have a question related to Data Security ?</h3>
    <span class="btn">REQUEST A QUOTE</span>
  </div>
</section>

<section class="posts">
  <div class="wrap">
    <p class="eyebrow">From Our Blog</p>
    <h2 class="title">Latest Posts</h2>
    <p class="lead">News, guides and practical tips on data, reporting and regulation.</p>
    <div class="post-grid">
      <article class="post-main">
        <div class="thumb" role="img" aria-label="Article image about getting ready for new EU data regulation"></div>
        <h3>Preparing your business for GDPR</h3>
        <div class="meta"><span>July 12, 2017</span><span>3 Comments</span></div>
        <p>A simple checklist for small companies reviewing how they collect, store and use personal data under the new rules.</p>
      </article>
      <div class="post-list">
        <div class="post-item"><div class="thumb" role="img" aria-label="Article thumbnail"></div><div><h4>Choosing a BI platform</h4><div class="meta"><span>July 10, 2017</span><span>2 Comments</span></div><p>What to look for before you commit to a tool.</p></div></div>
        <div class="post-item"><div class="thumb" role="img" aria-label="Article thumbnail"></div><div><h4>Reports people actually read</h4><div class="meta"><span>July 06, 2017</span><span>4 Comments</span></div><p>Keep reporting short, clear and useful.</p></div></div>
        <div class="post-item"><div class="thumb" role="img" aria-label="Article thumbnail"></div><div><h4>Data quality basics</h4><div class="meta"><span>July 02, 2017</span><span>1 Comment</span></div><p>Small fixes that make a large difference.</p></div></div>
        <div class="post-item"><div class="thumb" role="img" aria-label="Article thumbnail"></div><div><h4>Planning a data project</h4><div class="meta"><span>June 28, 2017</span><span>5 Comments</span></div><p>Set scope, owners and goals from day one.</p></div></div>
      </div>
    </div>
  </div>
</section>

<footer class="site-footer">
  <div class="wrap footer-grid">
    <div>
      <h4>Contact Us</h4>
      <ul>
        <li><svg width="12" height="14" viewBox="0 0 12 16"><path d="M6 0a6 6 0 00-6 6c0 4.5 6 10 6 10s6-5.5 6-10a6 6 0 00-6-6zm0 8.5A2.5 2.5 0 118.5 6 2.5 2.5 0 016 8.5z" fill="#1b6fc2"/></svg>12 Sample Street, Anytown, UK</li>
        <li><svg width="12" height="12" viewBox="0 0 24 24"><path fill="#1b6fc2" d="M6.6 10.8a15 15 0 006.6 6.6l2.2-2.2a1 1 0 011-.25 11 11 0 003.6.6 1 1 0 011 1V20a1 1 0 01-1 1A17 17 0 013 4a1 1 0 011-1h3.5a1 1 0 011 1 11 11 0 00.6 3.6 1 1 0 01-.25 1z"/></svg>+44 000 000 0000</li>
        <li><svg width="12" height="12" viewBox="0 0 24 24"><path fill="#1b6fc2" d="M6.6 10.8a15 15 0 006.6 6.6l2.2-2.2a1 1 0 011-.25 11 11 0 003.6.6 1 1 0 011 1V20a1 1 0 01-1 1A17 17 0 013 4a1 1 0 011-1h3.5a1 1 0 011 1 11 11 0 00.6 3.6 1 1 0 01-.25 1z"/></svg>+44 000 000 0001</li>
        <li><svg width="12" height="12" viewBox="0 0 24 24"><rect x="2" y="5" width="20" height="14" rx="2" fill="#1b6fc2"/></svg>info@meridata.co.uk</li>
      </ul>
    </div>
    <div>
      <h4>Newsletter</h4>
      <p style="font-size:12px">Subscribe to our newsletter to get the latest news and updates.</p>
      <div class="subscribe"><span class="input">Email address</span><span class="go">GO</span></div>
    </div>
    <div>
      <h4>Connect With Us</h4>
      <div class="socials"><i></i><i></i><i></i><i></i><i></i><i></i></div>
      <div class="footer-brand"><span class="brand-mark"></span><span>Meridata Ltd</span></div>
    </div>
  </div>
</footer>
<div class="bottom-bar">Copyright © Meridata Ltd. All rights reserved.</div>

</body>
</html>
```